Design home page for brightvane.xyz

We’re seeking a sleek, lead-generation-focused single-page website for Brightvane.xyz that communicates our expertise in delivering high-intent leads to mid-sized businesses. The goal is to guide visitors toward scheduling a free consultation while emphasizing our performance-based approach and comprehensive service offerings.

Industry/Entity Type

Marketing

Number of Pages Required

1 page

Font styles to use
Sans Serif

Requirements
Must have
• content from https://files.quorvalet.example/doc/7hTmwQRZa93KpLdVyxNe42UcBsFoGj8rYiMn5EkPtWz/view?tab=t.0
Nice to have
• color pallet from here https://files.quorvalet.example/doc/4pRkz-NWb62VxLeTyqJs8cHaDmFu3GiYoBnQ5tXeKv/view?tab=t.0

```html
<!DOCTYPE html>
<html lang="en">
<head>
<meta charset="utf-8">
<title>Brightvane.xyz — High Intent Leads</title>
<link rel="stylesheet" href="https://fonts.googleapis.com/css2?family=Outfit:wght@400;500;600;700;800&display=swap">
<style>
:root{
  --red:#a71c26;
  --red-dark:#8e1520;
  --ink:#1b1a22;
  --dark:#211a2b;
  --plum:#3e2b3d;
  --light:#f2f0f6;
  --muted:#6d6b76;
  --line:#e4e1ea;
  --white:#ffffff;
  --stage:#e4e4e6;
}
*{margin:0;padding:0;box-sizing:border-box}
html,body{width:1200px;height:4780px;overflow:hidden}
body{background:var(--stage);font-family:"Outfit",sans-serif;color:var(--ink)}
.page{position:absolute;left:96px;top:87px;width:1010px;height:4603px;background:var(--white);overflow:hidden}
.a{position:absolute}
.band{position:absolute;left:0;width:1010px}
.ph{position:absolute;border-radius:18px}
.eyebrow{font-size:9px;font-weight:600;color:var(--red);text-transform:uppercase;letter-spacing:.2px}
.h2{font-size:21px;font-weight:600;line-height:26px;color:var(--ink)}
.small{font-size:9px;line-height:12px;color:var(--muted)}
.btn{position:absolute;display:flex;align-items:center;justify-content:center;border-radius:8px;font-size:9px;font-weight:600}
.btn-dark{background:#111;color:#fff}
.btn-red{background:var(--red);color:#fff}
.center{text-align:center;left:0;width:1010px}

/* top bar */
.topbar{top:0;height:24px;background:var(--dark);color:#ddd;font-size:8.5px}
.topbar .dot{display:inline-block;width:6px;height:6px;border-radius:50%;background:var(--red);margin-right:5px;vertical-align:middle}
.soc{position:absolute;width:13px;height:13px;border-radius:50%;background:var(--red)}
/* nav */
.nav{top:24px;height:58px;background:#fff;border-bottom:1px solid var(--line)}
.logo{font-size:16px;font-weight:700;color:var(--ink)}
.navlinks{display:flex;gap:22px;font-size:9.5px;font-weight:500}
/* hero */
.hero{top:82px;height:443px;background:var(--red)}
.hero h1{font-size:34px;line-height:40px;font-weight:800;color:#fff}
.card{position:absolute;background:#fff;border-radius:14px}
/* tiles */
.tile{position:absolute;width:119px;height:126px;background:var(--light);border-radius:16px;text-align:center;font-size:11px;font-weight:600;line-height:14px}
.tile .ic{width:38px;height:38px;border-radius:50%;background:#fff;margin:22px auto 12px;display:flex;align-items:center;justify-content:center}
/* why */
.wcard{position:absolute;border:1px solid rgba(255,255,255,.12);border-radius:10px;padding:40px 16px 0;color:#fff}
.wcard h4{font-size:11px;font-weight:600;line-height:13px}
.wcard p{font-size:8.5px;line-height:10.5px;color:#8b8596;margin-top:4px}
.wcard .ic{position:absolute;left:16px;top:10px;width:26px;height:26px;border-radius:50%;background:var(--red)}
/* lead capture */
.lcard{position:absolute;width:115px;height:126px;border:1px solid rgba(255,255,255,.2);border-radius:14px;background:rgba(255,255,255,.04);color:#fff;text-align:center;font-size:10px;font-weight:600;line-height:13px}
.lcard .ic{width:64px;height:64px;border-radius:50%;background:#fff;border:4px solid var(--red);margin:-8px auto 10px;display:flex;align-items:center;justify-content:center}
/* process */
.pcard{position:absolute;top:2903px;width:216px;height:302px;border:1px solid var(--line);border-radius:16px;background:#fff}
.pcard .img{position:absolute;left:0;top:0;width:216px;height:182px;border-radius:16px 16px 0 0}
.pcard .num{position:absolute;left:20px;top:160px;width:46px;height:34px;background:var(--red);color:#fff;font-size:22px;font-weight:700;border-radius:6px;display:flex;align-items:center;justify-content:center}
.pcard h4{position:absolute;left:20px;top:208px;font-size:10.5px;font-weight:600}
.pcard p{position:absolute;left:20px;top:232px;width:176px;font-size:8.5px;line-height:11px;color:var(--muted)}
.pcard .ar{position:absolute;right:20px;top:266px;color:var(--red);font-size:10px}
/* accordion */
.acc{position:absolute;left:256px;width:496px;background:#fff;border:1px solid var(--line);border-radius:6px;font-size:11px;font-weight:600;text-align:center}
.acc .pm{position:absolute;right:12px;top:50%;transform:translateY(-50%);font-size:12px}
/* footer */
.footer{top:4258px;height:308px;background:var(--dark);color:#fff}
.fcol h5{font-size:10.5px;font-weight:600;margin-bottom:10px}
.fcol li{list-style:none;font-size:8.5px;line-height:20px;color:#c8c3d0}
.copy{top:4566px;height:37px;background:#0e0b12;color:#bbb;font-size:8.5px;display:flex;align-items:center;justify-content:center}
</style>
</head>
<body>
<div class="page">

  <!-- Top bar -->
  <div class="band topbar">
    <div class="a" style="left:36px;top:7px"><span class="dot"></span>712 Harrow Lane, Denver</div>
    <div class="a" style="left:182px;top:7px"><span class="dot"></span>hello@brightvane.xyz</div>
    <div class="a" style="left:690px;top:7px"><span class="dot"></span>Mon to Sat: 8:00 am - 7:00 pm</div>
    <div class="soc" style="left:911px;top:6px"></div>
    <div class="soc" style="left:931px;top:6px"></div>
    <div class="soc" style="left:951px;top:6px"></div>
    <div class="soc" style="left:971px;top:6px"></div>
  </div>

  <!-- Navigation -->
  <div class="band nav">
    <div class="a logo" style="left:163px;top:18px">brightvane.xyz</div>
    <nav class="a navlinks" style="left:304px;top:22px"><span>Home</span><span>About</span><span>Service</span><span>Pages</span><span>Shop</span><span>Blog</span></nav>
    <div class="btn" style="left:590px;top:18px;width:54px;height:20px;border:1px solid var(--line);border-radius:10px;font-size:7.5px;font-weight:500">Contact Us</div>
    <div class="a" style="left:684px;top:17px;width:22px;height:22px;border-radius:50%;background:var(--red)">
      <svg width="22" height="22" viewBox="0 0 22 22"><path d="M8 6l2 3-1.3 1.3c.7 1.5 1.7 2.5 3 3L13 12l3 2-1 2c-4 0-8-4-8-8z" fill="#fff"/></svg>
    </div>
    <div class="a" style="left:712px;top:17px;font-size:8px;color:var(--muted);line-height:10px">Call Anything<br><b style="font-size:11px;color:var(--ink);font-weight:600">(303) 555-0148</b></div>
    <svg class="a" style="left:814px;top:22px" width="12" height="12" viewBox="0 0 12 12"><circle cx="5" cy="5" r="3.6" fill="none" stroke="#222" stroke-width="1.3"/><path d="M8 8l3 3" stroke="#222" stroke-width="1.3"/></svg>
    <svg class="a" style="left:836px;top:22px" width="12" height="12" viewBox="0 0 12 12"><circle cx="6" cy="6" r="5.2" fill="none" stroke="#222" stroke-width="1.1"/><circle cx="6" cy="5" r="1.8" fill="none" stroke="#222" stroke-width="1.1"/><path d="M2.8 9.8c1.6-2 4.8-2 6.4 0" fill="none" stroke="#222" stroke-width="1.1"/></svg>
  </div>

  <!-- Hero -->
  <section class="band hero">
    <h1 class="a" style="left:163px;top:108px">High Intent Leads<br>Delivered Directly to<br>Your Pipeline</h1>
    <p class="a" style="left:163px;top:254px;width:330px;font-size:9px;line-height:18px;color:#f4d9db">Take the guesswork out of lead generation. We connect you with high intent prospects who are genuinely interested in what you offer, helping you grow your sales pipeline with ease.</p>
    <div class="btn" style="left:163px;top:317px;width:100px;height:28px;background:#fff;color:var(--red)">Get In Touch</div>
    <p class="a" style="left:163px;top:364px;width:240px;font-size:8.5px;line-height:11px;color:#fff;font-style:italic;font-weight:500">Let’s talk about how we can deliver the leads your business needs. Schedule a Free Call Today</p>
    <svg class="a" style="left:400px;top:296px" width="100" height="60" viewBox="0 0 100 60"><path d="M2 2l26 10-10 4-4 10z" fill="#fff"/><path d="M30 30c14 24 50 24 60 6" fill="none" stroke="#fff" stroke-width="1.2" stroke-dasharray="3 3"/></svg>

    <div class="card" style="left:534px;top:94px;width:93px;height:117px;background:#fff">
      <div class="ph" role="img" aria-label="Rocket launching from a target illustration" style="left:12px;top:10px;width:69px;height:97px;background:linear-gradient(160deg,#f1c9cc,#c62a33);border-radius:12px"></div>
    </div>
    <div class="card" style="left:653px;top:74px;width:193px;height:126px">
      <div class="a" style="left:16px;top:16px;font-size:9px;font-weight:600">Email Marketing Campaign</div>
      <div class="a" style="left:16px;top:40px;font-size:8px;line-height:22px;color:var(--muted)">• Click<br>• Impression<br>• Goal</div>
      <div class="a" style="left:86px;top:40px;font-size:8px;line-height:22px;font-weight:600">50%<br>60%<br>90%</div>
      <svg class="a" style="left:120px;top:38px" width="60" height="60" viewBox="0 0 60 60"><circle cx="30" cy="30" r="22" fill="none" stroke="#eee" stroke-width="7"/><circle cx="30" cy="30" r="22" fill="none" stroke="var(--red)" stroke-width="7" stroke-dasharray="55 140"/><circle cx="30" cy="30" r="22" fill="none" stroke="#7565c9" stroke-width="7" stroke-dasharray="0 55 40 140"/><circle cx="30" cy="30" r="22" fill="none" stroke="#f2b233" stroke-width="7" stroke-dasharray="0 95 20 140"/></svg>
      <div class="a" style="left:150px;top:-14px;width:36px;height:30px;border-radius:6px;background:#f2a623"></div>
    </div>
    <div class="card" style="left:534px;top:235px;width:102px;height:152px;overflow:hidden">
      <div class="a" style="left:14px;top:16px;font-size:8px;font-weight:600;line-height:10px">Conversation<br>Rate Increased</div>
      <div class="a" style="left:44px;top:60px;font-size:8px;color:#5c56b6;font-weight:600">+140%</div>
      <svg class="a" style="left:0;top:72px" width="102" height="80" viewBox="0 0 102 80"><path d="M0 10c20 0 24 18 44 14s30-20 58-8v64H0z" fill="#ea6a6f"/></svg>
    </div>
    <div class="card" style="left:653px;top:217px;width:150px;height:137px">
      <div class="a" style="left:14px;top:12px;font-size:8px;font-weight:600">Website Traffic</div>
      <svg class="a" style="left:14px;top:36px" width="124" height="88" viewBox="0 0 124 88">
        <g fill="#ecd8db"><rect x="2" y="30" width="10" height="58"/><rect x="22" y="20" width="10" height="68"/><rect x="42" y="40" width="10" height="48"/><rect x="62" y="26" width="10" height="62"/><rect x="82" y="44" width="10" height="44"/><rect x="102" y="30" width="10" height="58"/></g>
        <g fill="var(--red)"><rect x="2" y="40" width="10" height="20"/><rect x="22" y="30" width="10" height="30"/><rect x="42" y="20" width="10" height="40"/><rect x="62" y="38" width="10" height="22"/><rect x="82" y="34" width="10" height="26"/><rect x="102" y="42" width="10" height="18"/></g>
      </svg>
    </div>
  </section>

  <!-- About -->
  <section>
    <div class="a" style="left:148px;top:650px;width:120px;height:250px;border:1px solid #b9b2dc;border-radius:60px"></div>
    <div class="ph" role="img" aria-label="Team meeting around a table in a dark office" style="left:163px;top:594px;width:250px;height:328px;border-radius:40px;background:linear-gradient(160deg,#3a4657,#151b24 60%,#54432f);border:3px solid #111"></div>
    <div class="a" style="left:393px;top:637px;width:54px;height:232px;background:var(--red);border-radius:14px;display:flex;align-items:center;justify-content:center">
      <span style="transform:rotate(-90deg);white-space:nowrap;color:#fff;font-size:20px;font-weight:600;font-style:italic">At Brightvane.xyz</span>
    </div>
    <div class="a eyebrow" style="left:512px;top:592px">We deliver results, not promises</div>
    <h2 class="a h2" style="left:512px;top:610px;width:340px;line-height:25px">We specialize in providing conversion-ready leads that fuel sustainable business growth.</h2>
    <div class="a" style="left:512px;top:698px;width:320px">
      <div style="display:flex;gap:10px;margin-bottom:10px"><svg width="24" height="24" viewBox="0 0 24 24"><circle cx="12" cy="12" r="9" fill="none" stroke="var(--red)" stroke-width="1.5" stroke-dasharray="3 2"/><circle cx="12" cy="12" r="3.5" fill="var(--red)"/></svg><div><div style="font-size:11px;font-weight:600">Entrepreneur Led Expertise:</div><div class="small" style="font-size:8px;line-height:10px">Founded by seasoned entrepreneurs with proven lead generation success.</div></div></div>
      <div style="display:flex;gap:10px;margin-bottom:10px"><svg width="24" height="24" viewBox="0 0 24 24"><rect x="4" y="4" width="16" height="16" rx="4" fill="none" stroke="var(--red)" stroke-width="1.5"/><circle cx="12" cy="12" r="3" fill="var(--red)"/></svg><div><div style="font-size:11px;font-weight:600">Performance Based Model:</div><div class="small" style="font-size:8px;line-height:10px">No upfront costs we succeed only when you do.</div></div></div>
      <div style="display:flex;gap:10px"><svg width="24" height="24" viewBox="0 0 24 24"><circle cx="12" cy="8" r="3.5" fill="none" stroke="var(--red)" stroke-width="1.5"/><path d="M4 20c2-5 14-5 16 0" fill="none" stroke="var(--red)" stroke-width="1.5"/></svg><div><div style="font-size:11px;font-weight:600">Comprehensive Approach:</div><div class="small" style="font-size:8px;line-height:10px">From SEO to PPC campaigns and high value content creation, we manage it all.</div></div></div>
    </div>
    <div class="btn btn-dark" style="left:512px;top:825px;width:110px;height:30px">Discover More</div>
  </section>

  <!-- Services -->
  <section class="band" style="top:989px;height:566px;background:linear-gradient(90deg,var(--light) 60%,#f7e1e4)">
    <div class="a" role="img" aria-label="Faint network of people icons" style="left:780px;top:0;width:230px;height:340px;background:radial-gradient(circle at 70% 50%,#e7a7ad,transparent 70%);opacity:.7"></div>
    <div class="a eyebrow center" style="top:72px">Comprehensive end-to-end lead generation</div>
    <h2 class="a h2 center" style="top:88px">We handle everything needed to deliver high-quality<br>leads so you can focus on scaling your business.</h2>
    <div class="a" style="left:163px;top:172px;width:683px;height:332px;background:#fff;border:1px solid var(--line);border-radius:20px"></div>
  </section>
  <div class="tile" style="left:189px;top:1191px"><div class="ic"><svg width="20" height="20"><rect x="3" y="4" width="14" height="12" rx="2" fill="none" stroke="var(--red)" stroke-width="1.5"/><path d="M6 9h8M6 12h5" stroke="var(--red)"/></svg></div>Content<br>Creation:</div>
  <div class="tile" style="left:326px;top:1191px"><div class="ic"><svg width="20" height="20"><rect x="2" y="4" width="16" height="10" rx="1.5" fill="none" stroke="var(--red)" stroke-width="1.5"/><path d="M7 17h6" stroke="var(--red)" stroke-width="1.5"/></svg></div>Design &amp;<br>Development:</div>
  <div class="tile" style="left:463px;top:1191px"><div class="ic"><svg width="20" height="20"><rect x="2" y="4" width="14" height="10" rx="1.5" fill="none" stroke="#555" stroke-width="1.5"/><circle cx="14" cy="14" r="3.5" fill="none" stroke="var(--red)" stroke-width="1.5"/></svg></div>SEO &amp;<br>Social Media:</div>
  <div class="tile" style="left:189px;top:1337px"><div class="ic"><svg width="20" height="20"><rect x="3" y="3" width="14" height="14" rx="2" fill="none" stroke="var(--red)" stroke-width="1.5"/><path d="M6 13l3-3 2 2 3-4" fill="none" stroke="var(--red)" stroke-width="1.5"/></svg></div>PPC<br>Campaigns:</div>
  <div class="tile" style="left:326px;top:1337px"><div class="ic"><svg width="20" height="20"><rect x="3" y="3" width="14" height="14" rx="2" fill="none" stroke="var(--red)" stroke-width="1.5"/><circle cx="10" cy="10" r="3" fill="var(--red)"/></svg></div>SEO &amp;<br>Social Media:</div>
  <div class="ph" role="img" aria-label="Man working at a laptop in a bright office" style="left:600px;top:1189px;width:217px;height:277px;background:linear-gradient(160deg,#c9c6b6,#6d7686 55%,#2f4a7a)"></div>
  <div class="ph" role="img" aria-label="Colleague working on a laptop at a desk" style="left:463px;top:1337px;width:137px;height:129px;background:linear-gradient(160deg,#e3dcd5,#9a8c96 60%,#4b4f69);border:4px solid #fff"></div>

  <!-- Why choose -->
  <section>
    <div class="band" style="top:1601px;height:423px;background:var(--dark)"></div>
    <div class="a eyebrow" style="left:163px;top:1638px;font-size:8px">Why choose Brightvane.xyz?</div>
    <h2 class="a" style="left:163px;top:1652px;font-size:21px;font-weight:500;color:#fff">Brightvane.xyz?</h2>
    <p class="a" style="left:163px;top:1686px;width:240px;font-size:8.5px;line-height:10px;color:#8b8596">We specialize in delivering high-intent leads that drive measurable growth. Here’s how we stand out.</p>
    <div class="wcard" style="left:163px;top:1712px;width:158px;height:130px"><div class="ic"></div><h4>Results-Driven<br>Approach:</h4><p>We handle all aspects of lead generation, from creating lead magnets to executing advertising and SEO campaigns.</p></div>
    <div class="wcard" style="left:335px;top:1712px;width:143px;height:118px"><div class="ic"></div><h4>Tailored Strategies:</h4><p>Our campaigns are designed to connect you with prospects who are genuinely interested in the type of products or services you offer.</p></div>
    <div class="wcard" style="left:163px;top:1857px;width:149px;height:124px"><div class="ic"></div><h4>Simplified Growth<br>Solutions:</h4><p>With all the heavy lifting managed by our team, you can focus entirely on growing your business and closing more deals.</p></div>
    <div class="a" role="img" aria-label="Thoughtful man at a laptop in an open office" style="left:534px;top:1560px;width:476px;height:464px;border-radius:30px 0 0 0;background:linear-gradient(150deg,#eef0f2,#c7ccd4 45%,#5a6b86 75%,#2f3f5e)"></div>
  </section>

  <!-- Testimonial -->
  <section class="band" style="top:2024px;height:453px;background:var(--light)"></section>
  <div class="a eyebrow" style="left:163px;top:2142px;font-size:8px">Testimonial</div>
  <h2 class="a h2" style="left:163px;top:2158px;font-weight:500">What Customers are<br>Saying?</h2>
  <p class="a small" style="left:163px;top:2234px;width:235px;font-size:8.5px;line-height:17px">There are many variations of passages of Lorem Ipsum available, but the majority have suffered alterat some form, by injected humour.There are many variations of passages</p>
  <div class="btn btn-dark" style="left:163px;top:2324px;width:108px;height:30px">Discover More</div>
  <div class="a" style="left:484px;top:2120px;width:334px;height:60px;background:#fff;border:1px solid var(--line);border-radius:16px"></div>
  <div class="a" style="left:470px;top:2128px;width:362px;height:60px;background:#fff;border:1px solid var(--line);border-radius:16px"></div>
  <div class="a" style="left:456px;top:2139px;width:388px;height:248px;background:#fff;border:1px solid var(--line);border-radius:16px;box-shadow:0 6px 18px rgba(0,0,0,.04)"></div>
  <div class="a" style="left:645px;top:2132px;width:24px;height:24px;border-radius:50%;background:var(--red);color:#fff;font-size:11px;text-align:center;line-height:24px">↑</div>
  <div class="a" role="img" aria-label="Customer portrait" style="left:490px;top:2183px;width:24px;height:24px;border-radius:50%;background:#c9c3cc"></div>
  <div class="a" style="left:536px;top:2182px;font-size:10.5px;font-weight:600">Lena Okafor</div>
  <div class="a" style="left:536px;top:2198px;font-size:8px;color:var(--muted)">Driving Student</div>
  <svg class="a" style="left:748px;top:2180px" width="64" height="56" viewBox="0 0 64 56"><path d="M4 4c12 0 18 10 14 26-2 10-8 18-14 22M34 4c12 0 18 10 14 26-2 10-8 18-14 22" fill="none" stroke="#e8a3a8" stroke-width="1.6"/></svg>
  <div class="a" style="left:490px;top:2228px;font-size:10px;font-weight:600;font-style:italic">Flexible Classes Refers to the During Process</div>
  <p class="a" style="left:490px;top:2250px;width:330px;font-size:10px;line-height:24px;color:var(--muted);font-style:italic">Acquiring is knowledge free or skills through the free use of process the digital technologies and the hope internet. Flexible classes free Flexible</p>
  <div class="a" style="left:490px;top:2338px;color:var(--red);font-size:15px;letter-spacing:1px">★★★★★</div>
  <div class="a" style="left:740px;top:2377px;width:20px;height:20px;border-radius:50%;background:#fff;border:1px solid var(--line);color:var(--red);font-size:9px;text-align:center;line-height:18px;left:645px">↓</div>

  <!-- Lead capture -->
  <section class="band" style="top:2477px;height:285px;background:linear-gradient(100deg,#3a2839,#4a3147)">
    <div class="a eyebrow" style="left:163px;top:86px;color:#7a2c35">Lead magnets we build</div>
    <h2 class="a" style="left:163px;top:102px;font-size:20px;font-weight:600;color:#fff">High-Intent Lead Capture</h2>
    <p class="a" style="left:163px;top:134px;width:200px;font-size:8.5px;line-height:10px;color:#e3dbe3">We create custom crafted content tailored for your audience:</p>
    <div class="btn btn-red" style="left:163px;top:170px;width:108px;height:28px">Discover More</div>
  </section>
  <div class="lcard" style="left:467px;top:2488px"><div class="ic"><svg width="28" height="28"><rect x="5" y="4" width="18" height="20" rx="2" fill="none" stroke="var(--red)" stroke-width="1.8"/><path d="M9 10h10M9 14h10M9 18h6" stroke="var(--red)" stroke-width="1.5"/></svg></div>Guides and<br>eBooks</div>
  <div class="lcard" style="left:597px;top:2488px"><div class="ic"><svg width="28" height="28"><rect x="4" y="5" width="20" height="18" rx="2" fill="none" stroke="var(--red)" stroke-width="1.8"/><path d="M8 19v-4M12 19v-7M16 19v-5M20 19v-9" stroke="var(--red)" stroke-width="1.8"/></svg></div>Industry<br>Insights Reports</div>
  <div class="lcard" style="left:731px;top:2488px"><div class="ic"><svg width="28" height="28"><circle cx="14" cy="14" r="9" fill="none" stroke="var(--red)" stroke-width="1.8"/><path d="M14 14V5a9 9 0 0 1 9 9z" fill="var(--red)"/></svg></div>Infographics &amp;<br>Visual Guides</div>
  <div class="lcard" style="left:531px;top:2625px;height:119px"><div class="ic"><svg width="28" height="28"><rect x="6" y="3" width="16" height="22" rx="2" fill="none" stroke="var(--red)" stroke-width="1.8"/><path d="M10 9h8M10 13h8M10 17h5" stroke="var(--red)" stroke-width="1.5"/></svg></div>Glossary of<br>Industry Terms</div>
  <div class="lcard" style="left:664px;top:2625px;height:119px"><div class="ic"><svg width="28" height="28"><rect x="6" y="4" width="16" height="20" rx="2" fill="none" stroke="var(--red)" stroke-width="1.8"/><path d="M10 14l3 3 5-6" fill="none" stroke="var(--red)" stroke-width="1.8"/></svg></div>Checklist for<br>Best Practices</div>

  <!-- Process -->
  <div class="a eyebrow center" style="top:2815px">How we deliver high-quality leads</div>
  <h2 class="a h2 center" style="top:2833px;font-weight:700">Our streamlined process ensures you receive ready-to-<br>engage leads without the hassle:</h2>
  <div class="pcard" style="left:163px"><div class="img" role="img" aria-label="Dart in a red target with a red arrow chart" style="background:linear-gradient(150deg,#4f6f9a,#b9343c 60%,#e9dcdc)"></div><div class="num">01</div><h4>Precise Market Targeting:</h4><p>We start by understanding your ideal customer profile and identifying high-intent prospects in your market.</p><div class="ar">→</div></div>
  <div class="pcard" style="left:395px"><div class="img" role="img" aria-label="Content marketing words on a desk with a tablet" style="background:linear-gradient(150deg,#2c2b2f,#8c6b3f 55%,#e3d3b6)"></div><div class="num">02</div><h4>Customized Campaign Execution:</h4><p>We take the time to understand your audience, creating and running campaigns tailored to their interests, leveraging insights from advertising, SEO, and lead magnets.</p><div class="ar">→</div></div>
  <div class="pcard" style="left:628px"><div class="img" role="img" aria-label="Business team working together in an office" style="background:linear-gradient(150deg,#d9dce2,#5a5f6e 55%,#2b2f3a)"></div><div class="num">03</div><h4>All-Inclusive Management:</h4><p>From strategy to execution, we handle every detail, delivering leads while you focus on closing deals.</p><div class="ar">→</div></div>

  <!-- Sets us apart -->
  <section class="band" style="top:3258px;height:189px;background:var(--red);color:#fff;text-align:center">
    <div class="a center" style="top:30px;font-size:8px;font-weight:500">WHAT</div>
    <h2 class="a center" style="top:42px;font-size:21px;font-weight:600">Sets Us Apart?</h2>
    <p class="a center" style="top:72px;font-size:8.5px;line-height:11px">We’re more than just a lead generation service-our approach<br>ensures valuable opportunities for your business:</p>
    <div class="a center" style="top:112px;font-size:12px;font-weight:600">High-Intent Leads:</div>
    <p class="a center" style="top:130px;font-size:8.5px;line-height:11px">The high-intent leads we generate provide a solid starting point for<br>building meaningful connections.</p>
    <div class="btn" style="left:262px;top:108px;width:14px;height:38px;background:#fff;color:var(--ink);border-radius:3px;font-size:10px">‹</div>
    <div class="btn" style="left:734px;top:108px;width:14px;height:38px;background:#fff;color:var(--ink);border-radius:3px;font-size:10px">›</div>
  </section>

  <!-- Designed for you -->
  <div class="a eyebrow center" style="top:3485px;text-transform:none">Effortless Growth,</div>
  <h2 class="a h2 center" style="top:3499px">Designed for You</h2>
  <p class="a center" style="top:3528px;font-size:8.5px;line-height:11px;color:var(--muted)">We simplify lead generation, so you can focus on<br>growing your business</p>
  <div class="ph" role="img" aria-label="Two businessmen shaking hands at a desk" style="left:163px;top:3573px;width:312px;height:217px;border-radius:24px;background:linear-gradient(150deg,#eef0f2,#b4bac3 50%,#2d3440)"></div>
  <div class="a eyebrow" style="left:532px;top:3580px;text-transform:none">Hands</div>
  <h3 class="a" style="left:532px;top:3592px;font-size:15px;font-weight:600">Off Convenience:</h3>
  <p class="a small" style="left:532px;top:3615px;width:240px;font-size:8.5px;line-height:11px">We manage the strategy, content, advertising, and optimization, delivering a steady flow of high-quality prospects.</p>
  <div class="ph" role="img" aria-label="Hand stacking wooden blocks into a rising staircase" style="left:532px;top:3673px;width:314px;height:210px;border-radius:24px;background:linear-gradient(150deg,#1d2740,#3b4766 55%,#a0343a)"></div>
  <div class="a eyebrow" style="left:219px;top:3803px;text-transform:none">Built</div>
  <h3 class="a" style="left:219px;top:3815px;font-size:15px;font-weight:600">to Scale:</h3>
  <p class="a small" style="left:219px;top:3838px;width:230px;font-size:8.5px;line-height:11px">Our process adapts to your growth goals, ensuring consistent lead flow whether you’re starting small or scaling rapidly.</p>

  <!-- Success stories -->
  <section class="band" style="top:3935px;height:323px;background:var(--light)"></section>
  <div class="a eyebrow center" style="top:3979px">Proven</div>
  <h2 class="a h2 center" style="top:3993px">Success Stories</h2>
  <p class="a center" style="top:4022px;font-size:8.5px;line-height:11px;color:var(--muted)">Discover how our clients have achieved exceptional growth<br>with Brightvane.xyz</p>
  <div class="acc" style="top:4062px;height:54px;padding-top:8px">
    <div style="font-size:8.5px;font-weight:400;font-style:italic;color:var(--muted);line-height:11px">“Brightvane.xyz has completely transformed our lead generation efforts. We’ve<br>seen a 35% increase in high quality leads in just three months.”</div>
    <div style="color:var(--red);margin-top:4px">Marcus T., VP of Sales at a Mid-Sized B2B Firm</div>
    <span class="pm" style="color:var(--red)">–</span>
  </div>
  <div class="acc" style="top:4129px;height:33px;line-height:31px">Priya R., CEO of a Professional Services Company<span class="pm">+</span></div>
  <div class="acc" style="top:4176px;height:35px;line-height:33px">Oliver K., Marketing Director at a SaaS Company<span class="pm">+</span></div>

  <!-- Footer -->
  <footer class="band footer">
    <div class="a logo" style="left:163px;top:40px;color:#fff">brightvane.xyz</div>
    <div class="soc" style="left:729px;top:44px;width:18px;height:18px"></div>
    <div class="soc" style="left:761px;top:44px;width:18px;height:18px"></div>
    <div class="soc" style="left:793px;top:44px;width:18px;height:18px"></div>
    <div class="soc" style="left:826px;top:44px;width:18px;height:18px"></div>
    <div class="a" style="left:163px;top:129px;font-size:10.5px;font-weight:600;line-height:12px">Driving Real<br>Growth, One<br>Lead at a Time</div>
    <div class="a fcol" style="left:308px;top:129px"><h5>Link</h5><ul><li>Social Marketing</li><li>Paid Search Engine</li><li>Privacy Policy</li><li>Help</li></ul></div>
    <div class="a fcol" style="left:455px;top:129px"><h5>Contact</h5><ul><li>712 Harrow Lane, Denver</li><li><span style="color:var(--red)">●</span> (303) 555-0148</li><li><span style="color:var(--red)">●</span> hello@brightvane.xyz</li></ul></div>
    <div class="a fcol" style="left:629px;top:129px"><h5>Newsletter</h5></div>
    <div class="a" style="left:629px;top:163px;width:217px;height:31px;background:#0f0c14;border-radius:6px;font-size:8.5px;color:#8c8696;padding:10px 16px">Email address</div>
    <div class="btn btn-red" style="left:629px;top:203px;width:91px;height:32px;border-radius:10px">Subscribe</div>
  </footer>
  <div class="band copy">Copyright 2025 Brightvane.xyz, LLC. All rights reserved.</div>

</div>
</body>
</html>
```